Aesthetic shopify website with functioning mobile version

I need a website that looks aesthetically pleasing using the pictures, logos, and product that I provide in the files. I also need to have an aesthetic easy to use mobile version as well.

Here is a list of things I want included in the website.
- Shipping rates are surfaced during checkout
- Discount codes can be applied in the cart
- A shopper can edit their cart’s content
- There is an option for order status tracking
- An email notification is sent to confirm a purchase

The domain is www.brandelio.com, so I am not sure how to go forward with having you convert it to that domain. I look forward to working with you!

```html
<!DOCTYPE html>
<html lang="en">
<head>
<meta charset="utf-8">
<title>Brandelio — Curl Defining Cream</title>
<link href="https://fonts.googleapis.com/css2?family=Open+Sans:wght@400;600;700;800&family=Libre+Franklin:wght@400;500;600&display=swap" rel="stylesheet">
<style>
:root{
  --gold:#74633f;
  --gold-line:#7a6842;
  --ink:#1f1f1f;
  --text:#222;
  --muted:#f2f2f2;
  --footer:#1d1d1d;
  --white:#fff;
  --orange:#f7a93c;
  --btn-dark:#2e2f2a;
}
*{margin:0;padding:0;box-sizing:border-box}
html,body{width:1200px;height:3242px;overflow:hidden}
body{position:relative;font-family:"Libre Franklin",sans-serif;color:var(--text);background:var(--white)}
.abs{position:absolute}
.heading{font-family:"Open Sans",sans-serif;font-weight:800;text-transform:uppercase;letter-spacing:-0.5px}

/* hero */
.hero{left:0;top:0;width:1200px;height:680px;background:linear-gradient(100deg,#4d574c 0%,#596257 45%,#6f6c60 75%,#8a8473 100%)}
.brand-name{left:75px;top:38px;font-family:"Open Sans",sans-serif;font-weight:800;font-size:38px;color:var(--white);letter-spacing:0.5px}
.nav{left:436px;top:48px;display:flex;gap:0;align-items:center}
.nav a{font-family:"Open Sans",sans-serif;font-weight:600;font-size:11px;color:var(--white);text-decoration:none;text-transform:uppercase;padding:9px 14px}
.nav a.active{background:var(--gold)}
.nav-tools{left:1056px;top:55px;display:flex;gap:14px;align-items:center;color:#fff;font-size:10px;font-weight:700}
.hero-title{left:126px;top:278px;font-size:50px;line-height:62px;color:var(--white)}
.arrow{width:46px;height:46px}

/* section titles */
.section-title{width:1200px;text-align:center;font-size:30px;color:var(--ink)}
.rule{width:90px;height:3px;background:var(--gold-line);left:555px}

.ing-icon{width:40px;height:40px}
.ing-text{font-size:13px;line-height:24px;width:260px;color:#111}
.ing-text.right{text-align:right}

.featured{left:0;top:1208px;width:1200px;height:727px;background:var(--muted)}
.prod-box{left:165px;top:1389px;width:405px;height:382px;background:var(--white)}
.thumb{top:1783px;width:87px;height:85px;background:var(--white)}
.prod-name{left:598px;top:1402px;font-family:"Open Sans",sans-serif;font-weight:700;font-size:27px;color:#111}
.stars{left:599px;top:1440px;font-size:11px;color:#c9a233;letter-spacing:1px}
.stars span{color:#222;font-weight:600;letter-spacing:0;margin-left:6px;font-size:10px}
.price{left:599px;top:1462px;font-size:11px;font-weight:600}
.price s{color:#555;margin-right:3px}
.desc{left:599px;top:1505px;width:425px;font-size:12.5px;line-height:23.5px}
.qty-label{left:599px;top:1644px;font-size:11px}
.qty{left:599px;top:1664px;width:206px;height:44px;border:2px solid #222;display:flex}
.qty div{display:flex;align-items:center;justify-content:center;font-size:14px}
.qty .step{width:56px;font-weight:800;font-size:22px}
.qty .num{flex:1;border-left:2px solid #222;border-right:2px solid #222}
.add-cart{left:814px;top:1664px;width:205px;height:44px;background:#0e0e0e;color:#fff;display:flex;align-items:center;justify-content:center;gap:8px;font-family:"Open Sans",sans-serif;font-weight:700;font-size:14px}
.buy-now{left:601px;top:1721px;width:418px;height:49px;background:var(--btn-dark);color:#fff;display:flex;align-items:center;justify-content:center;font-family:"Open Sans",sans-serif;font-weight:700;font-size:18px}

/* email */
.email-band{left:0;top:1935px;width:1200px;height:289px;background:var(--gold)}
.email-title{top:1982px;font-size:40px;color:var(--white)}
.email-sub{top:2074px;width:1200px;text-align:center;font-family:"Open Sans",sans-serif;font-size:18px;color:var(--white)}
.field{background:var(--white);display:flex;align-items:center;padding-left:12px;font-family:"Open Sans",sans-serif;font-size:11px;color:#222}
.btn-black{background:#0e0e0e;color:#fff;display:flex;align-items:center;justify-content:center;font-family:"Open Sans",sans-serif;font-weight:700;font-size:14px}

/* promo */
.promo{left:0;top:2224px;width:1200px;height:544px;background:linear-gradient(180deg,#f9b247 0%,#f6a236 55%,#e08a2b 100%)}
.promo-title{top:2354px;font-size:42px;color:var(--white)}
.promo-sub{top:2422px;width:1200px;text-align:center;font-family:"Open Sans",sans-serif;font-size:18px;color:#fff4e0}
.shop-now{left:516px;top:2483px;width:170px;height:46px;background:var(--gold);color:#fff;display:flex;align-items:center;justify-content:center;font-family:"Open Sans",sans-serif;font-weight:700;font-size:17px}

/* footer */
.footer{left:0;top:2768px;width:1200px;height:474px;background:var(--footer)}
.foot-head{font-family:"Open Sans",sans-serif;font-weight:700;font-size:15px;color:#fff;text-transform:uppercase}
.foot-text{font-family:"Open Sans",sans-serif;font-size:14px;color:#fff;line-height:28px}
.social{top:2873px;width:32px;height:32px;border:1.5px solid #fff;border-radius:50%}
.btn-gold{background:var(--gold);color:#fff;display:flex;align-items:center;justify-content:center;font-family:"Open Sans",sans-serif;font-weight:700;font-size:13px}
.card{top:3132px;width:42px;height:26px;background:#fff;border-radius:3px;display:flex;align-items:center;justify-content:center}
.card i{display:block;width:26px;height:12px;border-radius:2px}
</style>
</head>
<body>

<!-- hero -->
<section class="abs hero" role="img" aria-label="Smiling man with curly hair beside two tubes of curl defining cream"></section>
<div class="abs brand-name">BRANDELIO</div>
<nav class="abs nav">
  <a class="active" href="#">Home</a><a href="#">About Us</a><a href="#">Products</a><a href="#">Ingredients</a><a href="#">Reviews</a><a href="#">Contact Us</a>
</nav>
<div class="abs nav-tools">
  <svg width="11" height="11" viewBox="0 0 12 12"><circle cx="5" cy="5" r="3.6" fill="none" stroke="#fff" stroke-width="1.8"/><line x1="7.8" y1="7.8" x2="11" y2="11" stroke="#fff" stroke-width="2"/></svg>
  <svg width="10" height="11" viewBox="0 0 10 11"><circle cx="5" cy="3" r="2.6" fill="#fff"/><path d="M0 11c0-4 2-5.5 5-5.5s5 1.5 5 5.5z" fill="#fff"/></svg>
  <span style="display:flex;align-items:center;gap:2px"><svg width="13" height="11" viewBox="0 0 13 11"><path d="M0 3h13l-1.5 7h-10z" fill="#fff"/><path d="M3 3l2-3M10 3l-2-3" stroke="#fff" stroke-width="1.2"/></svg>0</span>
</div>
<h1 class="abs heading hero-title">Welcome to the<br>Brandelio</h1>
<svg class="abs arrow" style="left:30px;top:317px" viewBox="0 0 46 46"><circle cx="23" cy="23" r="23" fill="#8f938c" opacity="0.75"/><path d="M27 13l-10 10 10 10" fill="none" stroke="#555" stroke-width="5"/></svg>
<svg class="abs arrow" style="left:1128px;top:317px" viewBox="0 0 46 46"><circle cx="23" cy="23" r="23" fill="#a39d90" opacity="0.75"/><path d="M19 13l10 10-10 10" fill="none" stroke="#666" stroke-width="5"/></svg>

<!-- key ingredients -->
<h2 class="abs heading section-title" style="left:0;top:738px">Key Ingredients</h2>
<div class="abs rule" style="top:799px"></div>
<div class="abs" style="left:522px;top:866px;width:154px;height:312px;background:linear-gradient(180deg,#2c2c2c,#1b1b1b 85%,#eee)" role="img" aria-label="Tube of curl defining cream"></div>

<div class="abs ing-icon" style="left:437px;top:857px;border:2px solid #b8924a;border-radius:6px" role="img" aria-label="Oil bottle icon"></div>
<p class="abs ing-text right" style="left:218px;top:904px">Simmondsia Chinensis (Jojoba) Seed Oil - Deep penetrating oil that softens and conditions</p>
<div class="abs ing-icon" style="left:437px;top:1005px;border:2px solid #b8924a;border-radius:50%" role="img" aria-label="Molecule icon"></div>
<p class="abs ing-text right" style="left:218px;top:1051px">Polyquaternium-11 - Plant- derived polymer to add volume and help thicken hai</p>
<div class="abs ing-icon" style="left:710px;top:857px;border:2px solid #b8924a;border-radius:50%" role="img" aria-label="Hair strand icon"></div>
<p class="abs ing-text" style="left:708px;top:904px;width:310px">Helianthus Annuus (Sunflower) Extract - Naturally-derived UV protectant for hair to&nbsp; prevent color fading, while also conditioning hair and adding shine</p>
<div class="abs ing-icon" style="left:710px;top:1003px;border:2px solid #b8924a;border-radius:6px" role="img" aria-label="Hair care icon"></div>
<p class="abs ing-text" style="left:708px;top:1051px;width:300px">Sed ut perspiciatis unde omnis iste natus error sit voluptatem accusantium doloremque laudantium, totam rem aperiam, eaque</p>

<!-- featured -->
<section class="abs featured"></section>
<h2 class="abs heading section-title" style="left:0;top:1269px">Featured Products</h2>
<div class="abs rule" style="top:1330px"></div>
<div class="abs prod-box"></div>
<div class="abs" style="left:282px;top:1434px;width:170px;height:300px;background:linear-gradient(180deg,#2c2c2c,#1b1b1b 85%,#f4f4f4)" role="img" aria-label="Tube of curl defining cream"></div>
<div class="abs thumb" style="left:219px"><div style="margin:10px auto;width:26px;height:64px;background:#262626" role="img" aria-label="Product thumbnail"></div></div>
<div class="abs thumb" style="left:325px"><div style="margin:10px auto;width:26px;height:64px;background:#262626" role="img" aria-label="Product thumbnail"></div></div>
<div class="abs thumb" style="left:430px"><div style="margin:14px auto;width:22px;height:56px;background:#262626" role="img" aria-label="Product thumbnail"></div></div>
<div class="abs prod-name">BRANDELIO</div>
<div class="abs stars">★★★★★<span>25 reviews</span></div>
<div class="abs price"><s>$150.00</s>$110.00</div>
<p class="abs desc">Lorem ipsum dolor sit amet, consectetscing el eiusmod tempor incididunt ut labore et dolore magna aliqua. Quis ipsum suspendisse ultrices gravida. Risus commodo viverra maecenas accan lacus vel is. Lorem ipsum dolor sit amet, consectetur adipiscing el eiusmod temporLorem ipsum dolor sit amet, consectetur adipiscing el eiusmod</p>
<div class="abs qty-label">Quantity</div>
<div class="abs qty"><div class="step">+</div><div class="num">1</div><div class="step">−</div></div>
<div class="abs add-cart"><svg width="15" height="13" viewBox="0 0 15 13"><path d="M0 1h3l2 7h8l2-5H4" fill="#fff"/><circle cx="6" cy="11" r="1.5" fill="#fff"/><circle cx="12" cy="11" r="1.5" fill="#fff"/></svg>ADD TO CART</div>
<div class="abs buy-now">BUY NOW</div>

<!-- email listing -->
<section class="abs email-band"></section>
<div class="abs" style="left:0;top:1935px;width:290px;height:289px;background:linear-gradient(90deg,#b9a58a,#c48a5a 45%,var(--gold) 100%)" role="img" aria-label="Woman with long curly hair pointing toward the signup form"></div>
<div class="abs" style="left:943px;top:1955px;width:257px;height:269px;background:linear-gradient(160deg,#2b2b2b,#1b1b1b)" role="img" aria-label="Tilted tube of curl defining cream"></div>
<h2 class="abs heading section-title email-title" style="left:0;color:#fff">Join Email Listing</h2>
<div class="abs rule" style="top:2051px;left:574px;width:52px;background:#fff"></div>
<p class="abs email-sub">Be the first to hear about new products and community events</p>
<div class="abs field" style="left:340px;top:2125px;width:402px;height:44px">Email Address</div>
<div class="abs btn-black" style="left:757px;top:2125px;width:103px;height:44px">SIGN UP</div>

<!-- promo -->
<section class="abs promo" role="img" aria-label="Woman with red curly hair looking upward"></section>
<h2 class="abs heading section-title promo-title" style="left:0;color:#fff">Sed ut perspiciatis unde</h2>
<p class="abs promo-sub">Lorem ipsum dolor sit amet, consectetur adipiscing elit purus,&nbsp; ultrices inporttitor in, accumsan</p>
<div class="abs shop-now">SHOP NOW</div>

<!-- footer -->
<footer class="abs footer"></footer>
<div class="abs foot-head" style="left:75px;top:2834px">Follow</div>
<div class="abs social" style="left:76px"></div>
<div class="abs social" style="left:116px"></div>
<div class="abs social" style="left:155px"></div>
<div class="abs social" style="left:195px"></div>
<p class="abs foot-text" style="left:76px;top:2930px;width:440px">Lorem ipsum dolor sit amet, consectetur adipiscing elit purus, ultrices in porttitor in, accumsan non quam.</p>
<div class="abs foot-head" style="left:616px;top:2834px">About Us</div>
<div class="abs foot-head" style="left:733px;top:2834px">Contact Us</div>
<div class="abs foot-head" style="left:868px;top:2834px">Search</div>
<p class="abs foot-text" style="left:616px;top:2887px">Sign up or our newsletter below to keep in touch with our community</p>
<div class="abs field" style="left:616px;top:2930px;width:248px;height:41px;padding-left:14px">First Name</div>
<div class="abs field" style="left:878px;top:2930px;width:248px;height:41px;padding-left:14px">Last Name</div>
<div class="abs field" style="left:616px;top:2983px;width:403px;height:41px;padding-left:14px">Email Address</div>
<div class="abs btn-gold" style="left:1029px;top:2983px;width:97px;height:41px">SIGN UP</div>
<p class="abs foot-text" style="left:618px;top:3054px;line-height:27px">Copyright © 2021. CompanyName<br>All Right Reserved</p>
<div class="abs card" style="left:616px"><i style="background:#1a2a7a"></i></div>
<div class="abs card" style="left:668px"><i style="background:#e5452d"></i></div>
<div class="abs card" style="left:720px;background:#2b7bd1"><i style="background:#fff;opacity:.35"></i></div>
<div class="abs card" style="left:772px"><i style="background:#1e3a8a"></i></div>
<div class="abs card" style="left:824px"><i style="background:#2563aa"></i></div>
<div class="abs card" style="left:876px"><i style="background:#f0a030"></i></div>

</body>
</html>
```